Vitalquorra.com

I need a web design for a Online Wellness Center based in Chicago, IL and it's called "Vitalquorra" We provide Health risk assessment to individuals and interventions. Our portal has a Health Activity tracker where our members record health activities and aerobic miles and biometric data. Our Online wellness center tracks the participant's progress toward health goals and awards points for completed activities.
I started working on this website but the designer was not able to designer a website which describes what we do. I need a fresh look on this project. I need a very attractive, responsive website which says what we do.
These are the things we do.
1. We provide Health Risk Assessments to individuals and Co-operations
2. We Provide Free health screenings to undeserved communities
3. Assist individuals access free or affordable medications
4. We ask providers/doctors to see (or do a complete physical) one individual free of charge once a year (those individuals who are no insured and don't have money to pay from their pocket)
5. Assist patient access lab work at low cost
Our goal is to provide services that will lower the cost of care for our members.

Here is the website: www.vitalquorra.com still underdevelopment. PLEASE DO NOT COPY THIS STYLE OF WEBSITE. IT'S A BAD DESIGN AND THAT IS WHY I'M RE-DESIGNING THE SITE

Target Market(s)

Health individuals between the age of 21 to 65 Plus years old. Insured and uninsured

Industry/Entity Type

Health And Wellness

Coding

Coded - Design and coding required

Number of Pages Required

5+ page

Colors
0292cd

Requirements
Must have
• I'm still working on this websiteHere is the menu: Home, About us, Services, Health Screening, Providers, Contacts
• Please see. www.vitalquorra.com
Nice to have
• Event calender
• Upcoming Event
• Medication
• Lab assist
• Providers/Free Clinics

```html
<!DOCTYPE html>
<html lang="en">
<head>
<meta charset="utf-8">
<title>Vitalquorra – Online Wellness Center</title>
<link href="https://fonts.googleapis.com/css2?family=Open+Sans:wght@400;600;700;800&display=swap" rel="stylesheet">
<style>
:root{
  --green:#7cb928;
  --green-dark:#5f9a17;
  --navy:#1c2c72;
  --navy-deep:#16235c;
  --ink:#333a45;
  --muted:#7a808a;
  --light:#f1f2f4;
  --line:#e2e4e8;
  --charcoal:#2e3034;
  --charcoal-deep:#232427;
  --white:#ffffff;
}
*{box-sizing:border-box;margin:0;padding:0}
html,body{width:1200px;height:3772px;overflow:hidden}
body{font-family:"Open Sans",Arial,sans-serif;color:var(--ink);background:var(--white);font-size:13px;line-height:1.6}
.wrap{width:1100px;margin:0 auto;position:relative}
.btn{display:inline-block;background:var(--green);color:var(--white);font-weight:700;font-size:13px;letter-spacing:.5px;padding:11px 26px;text-transform:uppercase}
.btn-outline{background:transparent;border:2px solid var(--white)}
.section-title{font-weight:800;text-transform:uppercase;text-align:center;font-size:26px;letter-spacing:.5px}
.check{display:inline-block;width:14px;height:14px;vertical-align:-2px;margin-right:8px}

/* top bar */
.topbar{height:28px;background:var(--green-dark);color:var(--white);font-size:11px}
.topbar .wrap{display:flex;justify-content:space-between;align-items:center;height:28px}
.topbar span{margin-right:18px}
.topbar .auth b{margin-left:18px;font-weight:700}

/* header */
.header{height:84px;background:var(--white);border-bottom:1px solid var(--line)}
.header .wrap{display:flex;justify-content:space-between;align-items:center;height:84px}
.logo{display:flex;align-items:center;font-size:28px;font-weight:700;color:var(--green)}
.logo i{display:inline-block;width:30px;height:30px;border-radius:50%;background:var(--green);margin-right:8px}
.nav a{color:var(--ink);font-size:13px;margin-left:38px;text-decoration:none}

/* hero */
.hero{height:408px;position:relative;background:linear-gradient(90deg,#eef2f6 0%,#dfe7ee 45%,#c9d6e2 100%)}
.hero-photo{position:absolute;right:0;top:0;width:640px;height:408px;background:linear-gradient(180deg,#d5e0ea,#b9c8d6 60%,#9fb2c4)}
.hero-copy{position:absolute;left:50px;top:120px}
.hero-copy h1{font-size:46px;font-weight:800;color:var(--navy);line-height:1.1}
.hero-copy h2{font-size:22px;font-weight:800;color:var(--navy);line-height:1.3;margin:12px 0 22px;text-transform:uppercase}
.hero-arrow{position:absolute;top:184px;width:30px;height:30px;border-radius:50%;background:rgba(124,185,40,.85)}
.hero-arrow svg{display:block;margin:8px}

/* services band */
.services{height:410px;background:var(--navy);color:var(--white);padding-top:70px}
.services .section-title{color:var(--green);font-size:22px}
.services .lead{text-align:center;width:900px;margin:22px auto 46px;font-size:12px;color:#d4d9ea}
.service-grid{display:grid;grid-template-columns:repeat(4,1fr);gap:40px}
.service h3{display:flex;align-items:center;color:var(--green);font-size:13px;font-weight:700;text-transform:uppercase;margin-bottom:10px}
.service h3 svg{margin-right:10px}
.service p{font-size:12px;color:#d4d9ea}

/* welcome */
.welcome{height:770px;padding-top:50px}
.welcome .section-title{color:var(--navy);font-size:24px}
.welcome .lead{text-align:center;width:1000px;margin:22px auto 0;font-size:12px;color:var(--muted)}
.welcome-photo{position:absolute;left:0;top:230px;width:330px;height:440px;background:linear-gradient(180deg,#e8eef3,#cfdbe5 55%,#7e9fc0)}
.welcome-list{position:absolute;left:470px;top:260px;width:620px}
.welcome-list h3{font-size:22px;font-weight:800;color:var(--navy);text-transform:uppercase;margin-bottom:20px}
.welcome-list li{list-style:none;font-size:13px;color:var(--muted);margin-bottom:14px;display:flex}

/* importance + providers */
.program{height:540px;background:linear-gradient(180deg,#2a3d66,#1e2c4d);color:var(--white);padding-top:54px}
.program .wrap{display:flex;justify-content:space-between}
.program h3{font-size:19px;font-weight:800;text-transform:uppercase;line-height:1.3}
.col-left{width:500px}
.col-right{width:500px;position:relative}
.program .intro{font-size:11px;color:#c8cfdd;margin:10px 0 18px}
.acc{background:var(--green);color:var(--white);font-size:11px;font-weight:700;text-transform:uppercase;padding:8px 14px;display:flex;justify-content:space-between;margin-bottom:8px}
.acc-body{padding:6px 14px 12px}
.acc-body li{list-style:none;font-size:11px;color:#dfe4ee;margin-bottom:9px}
.provider{display:flex;align-items:center;margin-bottom:18px}
.provider .avatar{width:96px;height:96px;border-radius:50%;border:4px solid var(--white);background:linear-gradient(180deg,#dfe5ec,#a9b7c7);flex:none;position:relative;z-index:1}
.provider .card{background:var(--white);color:var(--ink);margin-left:-26px;padding:12px 16px 12px 42px;width:320px;font-size:10px;line-height:1.5}
.provider .card b{display:block;color:var(--green);font-size:11px;margin-bottom:3px}
.program .view{position:absolute;right:0;bottom:6px;font-size:11px;padding:9px 20px}

/* medication */
.medication{height:280px;text-align:center;padding-top:64px}
.medication .kicker{color:var(--green);font-weight:800;font-size:28px}
.medication h2{color:var(--navy);font-weight:800;font-size:22px;text-transform:uppercase;margin-top:2px}
.medication p{font-size:11px;color:var(--muted);text-transform:uppercase;margin:4px 0 22px}

/* events */
.events{height:580px;background:var(--light);padding-top:60px}
.events .wrap{display:flex;justify-content:space-between}
.events h3{font-size:15px;font-weight:800;color:var(--navy);text-transform:uppercase;display:flex;align-items:center}
.events h3::after{content:"";flex:1;height:1px;background:#c9ccd2;margin-left:14px}
.ev-col{width:560px}
.event{display:flex;margin-top:34px}
.event .thumb{width:170px;height:110px;flex:none;background:linear-gradient(135deg,#7fa5cc,#3c6ea3)}
.event .thumb.alt{background:linear-gradient(135deg,#c5d4e2,#7e9ab7)}
.event .body{margin-left:22px}
.event .body b{color:var(--navy);font-size:12px;text-transform:uppercase}
.event .meta{font-size:10px;color:var(--green);margin:4px 0 8px}
.event .body p{font-size:11px;color:var(--muted)}
.cal-col{width:460px}
.calendar{margin-top:34px;background:var(--white);border:1px solid var(--line)}
.cal-head{display:flex;justify-content:space-between;align-items:center;background:#e6e8eb;height:42px}
.cal-head span{font-weight:700;font-size:12px;color:var(--ink);text-transform:uppercase}
.cal-head i{width:30px;height:42px;background:#c8ccd1;display:flex;align-items:center;justify-content:center}
table{width:100%;border-collapse:collapse}
th{font-size:11px;font-weight:600;color:var(--muted);height:34px}
td{text-align:center;height:48px;font-size:12px;color:var(--ink);border:6px solid var(--white);background:#eef0f2}
td.off{color:#b7bbc1}
td.today{background:var(--green);color:var(--white)}

/* lab assist */
.lab{height:320px;background:linear-gradient(180deg,#5d6166,#45484d);text-align:center;color:var(--white);padding-top:58px}
.lab h2{font-size:34px;font-weight:800}
.lab h3{font-size:18px;font-weight:800;color:var(--green);text-transform:uppercase;margin-top:4px}
.lab p{font-size:11px;color:#d8dadd;text-transform:uppercase;margin:6px 0 24px}

/* footer */
.footer{height:300px;background:var(--charcoal);color:#b4b7bc;padding-top:46px}
.footer .wrap{display:grid;grid-template-columns:repeat(4,1fr);gap:40px}
.footer h4{color:var(--white);font-size:11px;font-weight:700;text-transform:uppercase;margin-bottom:16px}
.footer li{list-style:none;font-size:10px;margin-bottom:10px;line-height:1.4}
.footer li em{display:block;font-style:normal;color:#7d8187}
.newsletter input{width:100%;height:34px;border:0;background:#45484d;margin:6px 0 10px}
.newsletter .btn{font-size:10px;padding:8px 20px}
.social{margin-top:22px;display:flex;gap:8px}
.social i{width:22px;height:22px;border-radius:50%;background:#4a4d52}
.bottombar{height:52px;background:var(--charcoal-deep);color:#8d9096;font-size:10px}
.bottombar .wrap{display:flex;justify-content:space-between;align-items:center;height:52px}
.bottombar a{color:#8d9096;text-decoration:none;margin-right:26px}
</style>
</head>
<body>

<div class="topbar">
  <div class="wrap">
    <div><span>Call us Today: +1 (312) 555-0148</span><span>info@vitalquorra.com</span></div>
    <div class="auth"><b>LOGIN</b><b>REGISTER</b></div>
  </div>
</div>

<header class="header">
  <div class="wrap">
    <div class="logo"><i></i>Vitalquorra</div>
    <nav class="nav">
      <a href="#">Home</a><a href="#">About us</a><a href="#">Services</a><a href="#">Health Screening</a><a href="#">Providers</a><a href="#">Contacts</a>
    </nav>
  </div>
</header>

<section class="hero">
  <div class="hero-photo" role="img" aria-label="Smiling doctor with stethoscope in front of a medical team"></div>
  <div class="hero-copy">
    <h1>WE PROVIDE</h1>
    <h2>Health risk assessment to individuals<br>and interventions</h2>
    <span class="btn">Signup now</span>
  </div>
  <span class="hero-arrow" style="left:14px"><svg width="14" height="14" viewBox="0 0 14 14"><path d="M9 2 4 7l5 5" stroke="#fff" stroke-width="2" fill="none"/></svg></span>
  <span class="hero-arrow" style="right:14px"><svg width="14" height="14" viewBox="0 0 14 14"><path d="M5 2l5 5-5 5" stroke="#fff" stroke-width="2" fill="none"/></svg></span>
</section>

<section class="services">
  <div class="wrap">
    <h2 class="section-title">Our wellness services</h2>
    <p class="lead">Vitalquorra is an online wellness center. Our objective is to make it easier to reach care and every day wellness, with clear help for members of all ages. We offer health risk assessments, free screenings, low cost lab work and help with affordable medication, and we work with local providers so that insured and uninsured people can take a first step toward better health.</p>
    <div class="service-grid">
      <div class="service"><h3><svg width="22" height="22" viewBox="0 0 22 22"><rect x="2" y="5" width="18" height="13" rx="2" fill="none" stroke="#7cb928" stroke-width="2"/><path d="M11 8v7M7.5 11.5h7" stroke="#7cb928" stroke-width="2"/></svg>Medication</h3><p>One of our trusted pharmacies will help you find affordable medication quickly in your neighborhood.</p></div>
      <div class="service"><h3><svg width="22" height="22" viewBox="0 0 22 22"><path d="M2 12h5l2-5 4 9 2-4h5" stroke="#7cb928" stroke-width="2" fill="none"/></svg>Health screening</h3><p>One of our licensed partners will run a free health screening near you at your fingertips.</p></div>
      <div class="service"><h3><svg width="22" height="22" viewBox="0 0 22 22"><path d="M8 2h6M9 2v7l-5 9a2 2 0 0 0 2 3h10a2 2 0 0 0 2-3l-5-9V2" stroke="#7cb928" stroke-width="2" fill="none"/></svg>Lab test</h3><p>One of our trusted labs will process your test at low cost and share results with you.</p></div>
      <div class="service"><h3><svg width="22" height="22" viewBox="0 0 22 22"><path d="M11 19s-8-5-8-10a4 4 0 0 1 8-1 4 4 0 0 1 8 1c0 5-8 10-8 10z" stroke="#7cb928" stroke-width="2" fill="none"/></svg>Wellness products</h3><p>One of our selected partners will offer wellness products to support your daily health goals.</p></div>
    </div>
  </div>
</section>

<section class="welcome">
  <div class="wrap">
    <h2 class="section-title">Welcome to Vitalquorra</h2>
    <p class="lead">By joining Vitalquorra, you track activities, aerobic miles and biometric data in one place and earn points for every completed step. Our members come from many backgrounds and every one of them gets the same support, whether insured or not. We work with local clinics and doctors across Chicago to make care easier to reach, and we help you stay on track with your personal goals while we keep the cost of care low.</p>
    <div class="welcome-photo" role="img" aria-label="Nurse in blue scrubs with crossed arms"></div>
    <div class="welcome-list">
      <h3>Our wellness services</h3>
      <ul>
        <li><svg class="check" viewBox="0 0 14 14"><path d="M2 7l3 3 7-7" stroke="#7cb928" stroke-width="2.4" fill="none"/></svg>We provide Health Risk Assessments to individuals and Co-operations</li>
        <li><svg class="check" viewBox="0 0 14 14"><path d="M2 7l3 3 7-7" stroke="#7cb928" stroke-width="2.4" fill="none"/></svg>We provide free health screenings to underserved communities</li>
        <li><svg class="check" viewBox="0 0 14 14"><path d="M2 7l3 3 7-7" stroke="#7cb928" stroke-width="2.4" fill="none"/></svg>Assist individuals access free or affordable medications</li>
        <li><svg class="check" viewBox="0 0 14 14"><path d="M2 7l3 3 7-7" stroke="#7cb928" stroke-width="2.4" fill="none"/></svg><span>We ask providers to see or do a complete physical for one individual free of charge once a year, for those who are not insured and cannot pay from their pocket</span></li>
        <li><svg class="check" viewBox="0 0 14 14"><path d="M2 7l3 3 7-7" stroke="#7cb928" stroke-width="2.4" fill="none"/></svg>Assist patients access lab work at low cost</li>
      </ul>
    </div>
  </div>
</section>

<section class="program" role="img" aria-label="Dimmed hospital corridor background">
  <div class="wrap">
    <div class="col-left">
      <h3>Importance of pursuing wellness<br>program</h3>
      <p class="intro">Why an individual and employer wellness program matters to everyday health</p>
      <div class="acc"><span>Why wellness program?</span><span>–</span></div>
      <ul class="acc-body">
        <li>✓ To reduce stress</li>
        <li>✓ To build healthy daily habits</li>
        <li>✓ To decrease personal health costs</li>
        <li>✓ To lower the risk of chronic disease</li>
        <li>✓ To feel stronger and have a higher quality of life</li>
        <li>✓ To stay in healthy life</li>
        <li>✓ To reduce preventable illnesses</li>
        <li>✓ To stay fit</li>
      </ul>
      <div class="acc"><span>Why employers should act?</span><span>+</span></div>
      <div class="acc"><span>How we help you</span><span>+</span></div>
    </div>
    <div class="col-right">
      <h3>Providers</h3>
      <p class="intro">Free clinics and doctors who offer a yearly check</p>
      <div class="provider"><div class="avatar" role="img" aria-label="Provider portrait"></div><div class="card"><b>Lakeshore Family Care Clinic</b>412 W. Harlow Street<br>Suite 200, Chicago, IL 60614, United States<br>(312) 555-0172</div></div>
      <div class="provider"><div class="avatar" role="img" aria-label="Provider portrait"></div><div class="card"><b>Lakeshore Family Care Clinic</b>412 W. Harlow Street<br>Suite 200, Chicago, IL 60614, United States<br>(312) 555-0172</div></div>
      <div class="provider"><div class="avatar" role="img" aria-label="Provider portrait"></div><div class="card"><b>Lakeshore Family Care Clinic</b>412 W. Harlow Street<br>Suite 200, Chicago, IL 60614, United States<br>(312) 555-0172</div></div>
      <span class="btn view">View more</span>
    </div>
  </div>
</section>

<section class="medication">
  <div class="kicker">MEDICATION</div>
  <h2>Vitalquorra provides you affordable medication</h2>
  <p>We make it as easy as possible to get your medication once you sign up</p>
  <span class="btn">Signup now</span>
</section>

<section class="events">
  <div class="wrap">
    <div class="ev-col">
      <h3>Upcoming health screening events</h3>
      <div class="event"><div class="thumb" role="img" aria-label="Medical screening equipment"></div><div class="body"><b>Health sample</b><div class="meta">12.04.2015 · November 16</div><p>Health screenings are free for members in our local community. Bring a friend and learn your numbers, get tips from our team and book a follow up visit in minutes at the center.</p></div></div>
      <div class="event"><div class="thumb alt" role="img" aria-label="Doctors reviewing results"></div><div class="body"><b>Health sample</b><div class="meta">12.04.2015 · November 24</div><p>Health screenings are free for members in our local community. Bring a friend and learn your numbers, get tips from our team and book a follow up visit in minutes at the center.</p></div></div>
    </div>
    <div class="cal-col">
      <h3>Our screening schedule</h3>
      <div class="calendar">
        <div class="cal-head"><i><svg width="10" height="10" viewBox="0 0 10 10"><path d="M7 1 3 5l4 4" stroke="#fff" stroke-width="2" fill="none"/></svg></i><span>November</span><i><svg width="10" height="10" viewBox="0 0 10 10"><path d="M3 1l4 4-4 4" stroke="#fff" stroke-width="2" fill="none"/></svg></i></div>
        <table>
          <tr><th>Su</th><th>Mo</th><th>Tu</th><th>We</th><th>Th</th><th>Fr</th><th>Sa</th></tr>
          <tr><td class="off">26</td><td class="off">27</td><td class="off">28</td><td class="off">29</td><td class="off">30</td><td class="off">31</td><td>1</td></tr>
          <tr><td>2</td><td>3</td><td>4</td><td>5</td><td>6</td><td>7</td><td>8</td></tr>
          <tr><td>9</td><td>10</td><td>11</td><td>12</td><td>13</td><td>14</td><td>15</td></tr>
          <tr><td>16</td><td>17</td><td>18</td><td>19</td><td>20</td><td>21</td><td>22</td></tr>
          <tr><td>23</td><td class="today">24</td><td>25</td><td>26</td><td>27</td><td>28</td><td>29</td></tr>
          <tr><td>30</td><td class="off">1</td><td class="off">2</td><td class="off">3</td><td class="off">4</td><td class="off">5</td><td class="off">6</td></tr>
        </table>
      </div>
    </div>
  </div>
</section>

<section class="lab" role="img" aria-label="Muted laboratory background">
  <h2>LAB ASSIST</h2>
  <h3>Lorem ipsum es simplemente el texto de relleno de las imprentas</h3>
  <p>Lorem ipsum es simplemente el texto de relleno de las imprentas y archivos de texto</p>
  <span class="btn btn-outline">Signup now</span>
</section>

<footer class="footer">
  <div class="wrap">
    <div><h4>Recent events</h4><ul>
      <li>Screening day at the north clinic<em>2 days ago</em></li>
      <li>Free blood pressure check<em>5 days ago</em></li>
      <li>Community lab work morning<em>1 week ago</em></li>
      <li>Healthy heart walk in the park<em>2 weeks ago</em></li>
    </ul></div>
    <div><h4>Recent news</h4><ul>
      <li>New partner clinics join our network<em>3 days ago</em></li>
      <li>Tips for a better yearly check<em>6 days ago</em></li>
      <li>Members reach a new points record<em>2 weeks ago</em></li>
    </ul></div>
    <div><h4>Recent news</h4><ul>
      <li>Vitalquorra</li>
      <li>412 W. Harlow Street<br>Chicago, IL 60614, USA</li>
      <li>+1 (312) 555-0148</li>
      <li>info@vitalquorra.com</li>
    </ul></div>
    <div class="newsletter"><h4>Newsletter</h4><ul><li>Get our latest updates through your email</li></ul>
      <input type="text" aria-label="Email">
      <span class="btn">Subscribe</span>
      <div class="social"><i></i><i></i><i></i><i></i><i></i></div>
    </div>
  </div>
</footer>

<div class="bottombar">
  <div class="wrap">
    <div><a href="#">Home</a><a href="#">About us</a><a href="#">Services</a><a href="#">Health Screening</a><a href="#">Providers</a><a href="#">Contacts</a></div>
    <div>© 2015 Vitalquorra. All rights reserved.</div>
  </div>
</div>

</body>
</html>
```